Email Signature

Our company is having its 10th anniversary in 2021. We would like a new email signature to celebrate the occasion. Attached is our business card design.
Please refer to our website for actual contact details.
www.corvanhold.com.au

Industry/Entity Type

Real Estate

Requirements
Must have
• Our logo
Email
Contact Numbers
Address
Website address

Celebrating 10 years in 2021
Nice to have
• Something that blends the designs of our website and business card

```html
<!DOCTYPE html>
<html lang="en">
<head>
<meta charset="utf-8">
<title>Corvan Hold – Email Signature</title>
<link rel="stylesheet" href="https://fonts.googleapis.com/css2?family=Exo+2:wght@700&family=Open+Sans:wght@400;600;700&display=swap">
<style>
  :root {
    --stage: #3b3b3b;
    --paper: #fbfbfb;
    --brand-blue: #1f6db3;
    --ink: #2b2b2b;
    --rule: #8a8a8a;
    --party-a: #f4d9ec;
    --party-b: #d9d4f3;
    --party-c: #e6f2df;
    --party-d: #f6e2c8;
  }
  * { box-sizing: border-box; margin: 0; padding: 0; }
  html, body { width: 1200px; height: 960px; overflow: hidden; }
  body {
    background: var(--stage);
    position: relative;
    font-family: "Open Sans", Arial, sans-serif;
    color: var(--ink);
  }
  .signature {
    position: absolute;
    left: 116px; top: 324px;
    width: 968px; height: 311px;
    background: var(--paper);
  }
  .brand {
    position: absolute;
    left: 40px; top: 170px;
    width: 254px;
    text-align: center;
  }
  .brand-name {
    font-family: "Open Sans", Arial, sans-serif;
    font-weight: 700;
    font-size: 30px;
    letter-spacing: 0.5px;
    color: var(--brand-blue);
    white-space: nowrap;
  }
  .social-links {
    display: flex;
    justify-content: center;
    gap: 5px;
    margin-top: 10px;
  }
  .social-dot {
    width: 21px; height: 21px;
    border-radius: 50%;
    background: var(--brand-blue);
  }
  .divider {
    position: absolute;
    left: 316px; top: 74px;
    width: 1px; height: 163px;
    background: var(--rule);
  }
  .person {
    position: absolute;
    left: 351px; top: 73px;
  }
  .person-name {
    font-family: "Exo 2", "Open Sans", sans-serif;
    font-weight: 700;
    font-size: 20px;
    color: var(--brand-blue);
    letter-spacing: 1px;
    line-height: 22px;
  }
  .person-role {
    font-size: 16px;
    line-height: 20px;
    color: var(--ink);
  }
  .contact-list {
    list-style: none;
    margin-top: 14px;
  }
  .contact-item {
    display: flex;
    align-items: center;
    height: 21.3px;
    font-size: 16px;
    color: var(--ink);
    white-space: nowrap;
  }
  .contact-icon {
    width: 14px; height: 14px;
    margin-right: 10px;
    fill: var(--brand-blue);
  }
  .bunting-art {
    position: absolute;
    left: 734px; top: 0;
    width: 234px; height: 62px;
    background: linear-gradient(90deg, var(--party-a), var(--party-c), var(--party-d), var(--party-b));
  }
  .anniversary-badge {
    position: absolute;
    left: 772px; top: 82px;
    width: 160px; height: 150px;
    border-radius: 12px;
    background: radial-gradient(circle at 50% 55%, var(--party-b) 0%, var(--party-a) 55%, var(--paper) 100%);
  }
</style>
</head>
<body>
  <section class="signature">
    <div class="brand">
      <div class="brand-name">CORVAN HOLD</div>
      <div class="social-links">
        <span class="social-dot"></span>
        <span class="social-dot"></span>
        <span class="social-dot"></span>
        <span class="social-dot"></span>
      </div>
    </div>

    <div class="divider"></div>

    <div class="person">
      <div class="person-name">DANIEL K, MARLOWE</div>
      <div class="person-role">Owner</div>
      <ul class="contact-list">
        <li class="contact-item">
          <svg class="contact-icon" viewBox="0 0 14 14"><path d="M4 1h6a1 1 0 0 1 1 1v10a1 1 0 0 1-1 1H4a1 1 0 0 1-1-1V2a1 1 0 0 1 1-1zm0.6 1.6v8h4.8v-8z"/></svg>
          1300 00CORV (2678)
        </li>
        <li class="contact-item">
          <svg class="contact-icon" viewBox="0 0 14 14"><path d="M3.2 1.5l2 2.4-1.1 1.4c.8 1.7 2.2 3.1 3.9 3.9l1.4-1.1 2.4 2-1.3 2.1C6 11.9 2.1 8 1.8 3l1.4-1.5z"/></svg>
          8027 3149
        </li>
        <li class="contact-item">
          <svg class="contact-icon" viewBox="0 0 14 14"><path d="M1 3h12v8H1zm1.2 1.1v.3L7 7.6l4.8-3.2v-.3zM2.2 5.8v4h9.6v-4L7 9z"/></svg>
          admin@corvanhold.com.au
        </li>
        <li class="contact-item">
          <svg class="contact-icon" viewBox="0 0 14 14"><path d="M7 1a6 6 0 1 1 0 12A6 6 0 0 1 7 1zm-4.6 5.3h2.3c.1-1.6.5-3 1.1-3.9a4.8 4.8 0 0 0-3.4 3.9zm0 1.4a4.8 4.8 0 0 0 3.4 3.9c-.6-.9-1-2.3-1.1-3.9zm3.7 0c.1 1.9.6 3.4.9 3.9.3-.5.8-2 .9-3.9zm0-1.4h1.8c-.1-1.9-.6-3.4-.9-3.9-.3.5-.8 2-.9 3.9zm3.2 0h2.3a4.8 4.8 0 0 0-3.4-3.9c.6.9 1 2.3 1.1 3.9zm2.3 1.4H9.3c-.1 1.6-.5 3-1.1 3.9a4.8 4.8 0 0 0 3.4-3.9z"/></svg>
          www.corvanhold.com.au
        </li>
        <li class="contact-item">
          <svg class="contact-icon" viewBox="0 0 14 14"><path d="M7 .8a4.6 4.6 0 0 1 4.6 4.6C11.6 9 7 13.4 7 13.4S2.4 9 2.4 5.4A4.6 4.6 0 0 1 7 .8zm0 2.7a1.9 1.9 0 1 0 0 3.8 1.9 1.9 0 0 0 0-3.8z"/></svg>
          Shop 8/17 Harbour Drive, Ryde, NSW 2112
        </li>
      </ul>
    </div>

    <div class="bunting-art" role="img" aria-label="Strings of colourful party bunting flags with streamers"></div>
    <div class="anniversary-badge" role="img" aria-label="Festive 10th anniversary emblem with balloons, confetti and a purple Happy Anniversary ribbon"></div>
  </section>
</body>
</html>
```